Flyer-Design für Wandschränke
Zielgruppe
Wir haben ein Profil entwickelt, welches es ermöglicht Schränke flächenbündig in Wände einzubauen. Das Profil ist aus MDF (Mitteldichte Holzfaserplatte) hergestellt und wird mit einer speziellen Fräsung versehen. Dieses Profil wird dann am Schrank befestigt und dient der Aufnahme der Gipskartonplatte. Der Name lautet RAHMO 2.0 Design Max Feldbauer. Das profil selbst ist zum Patent angemeldet. Unsere Zielgruppe sind Möbelhäuser und Küchenstudios.
Aufgabenstellung
Im Flyer sollte die Konstruktion und das fertige Produkt erkenbar sein. Der Flyer könnte DIN A4 sein, muss aber nicht!

```html
<!DOCTYPE html>
<html lang="de">
<head>
<meta charset="utf-8">
<title>RAHMO 2.0 – Lüftung als Designelement</title>
<link href="https://fonts.googleapis.com/css2?family=Nunito+Sans:wght@300;400&display=swap" rel="stylesheet">
<style>
  :root{
    --stage:#a39f9d;
    --paper:#ffffff;
    --ink:#1c1c1c;
    --text:#2a2a2a;
    --frame:#ffffff;
    --brand-square:#1c1c1c;
  }
  *{margin:0;padding:0;box-sizing:border-box}
  html,body{width:1200px;height:882px;overflow:hidden;background:var(--stage)}
  body{position:relative;font-family:"Nunito Sans",sans-serif;color:var(--text)}
  .sheet{position:absolute;left:28px;width:1143px;background:var(--paper);overflow:hidden}
  .sheet--outside{top:8px;height:419px}
  .sheet--inside{top:447px;height:420px}
  .photo{position:absolute}
  .photo--panel-edge{left:0;top:0;width:212px;height:419px;
    background:linear-gradient(180deg,#2a2420 0%,#1a1512 25%,#8a6a4e 55%,#3b2a20 75%,#2a1d16 100%)}
  .photo--portrait{left:840px;top:100px;width:303px;height:200px;
    background:linear-gradient(90deg,#b8b8b8 0%,#8e8e8e 30%,#2e2e2e 50%,#3a3a3a 65%,#c9c9c9 85%,#a9a9a9 100%)}
  .photo--profile-detail{left:362px;top:0;width:209px;height:420px;
    background:linear-gradient(90deg,#1c1e20 0%,#2a2d30 50%,#1a1a1a 62%,#d9c8a6 70%,#2b2d2f 84%,#4a4d50 100%)}
  .photo--kitchen{left:571px;top:0;width:572px;height:420px;
    background:linear-gradient(180deg,#8f8a86 0%,#d8d4cf 18%,#eeece9 40%,#f4f3f1 60%,#b9b6b2 78%,#5e5b58 100%)}
  .photo--vent-detail{left:973px;top:236px;width:138px;height:163px;
    background:linear-gradient(168deg,#f1f1f1 0%,#f1f1f1 32%,#2a2a2a 40%,#6a6a6a 48%,#2f2f2f 56%,#3c3c3c 100%)}
  .frame-line{position:absolute;inset:0;pointer-events:none}
  .headline{font-weight:400;color:var(--ink);letter-spacing:.01em;text-transform:uppercase;white-space:nowrap}
  .headline--cover{position:absolute;right:23px;top:70px;font-size:19px}
  .brand{position:absolute;background:var(--paper);display:flex;align-items:center;gap:8px;padding:6px 8px}
  .brand__mark{width:40px;height:40px;background:var(--brand-square);flex:none}
  .brand__name{font-weight:400;color:var(--ink);font-size:17px;line-height:1.15;letter-spacing:.02em}
  .brand--cover{left:721px;top:258px;width:292px;height:72px}
  .brand--inside{left:582px;top:27px;width:228px;height:54px}
  .brand--inside .brand__mark{width:32px;height:32px}
  .brand--inside .brand__name{font-size:13.5px}
  .contact{position:absolute;left:254px;top:302px;font-size:12.6px;line-height:16px;font-weight:300;color:var(--text);font-style:normal}
  .copy{position:absolute;left:39px;width:281px}
  .copy--intro{top:45px}
  .copy--profile{top:283px}
  .copy h2{font-weight:400;font-size:17.5px;color:var(--ink);text-transform:uppercase;margin-bottom:8px;white-space:nowrap}
  .copy p{font-size:12.3px;line-height:16.1px;font-weight:300;text-align:justify;hyphens:auto;padding-left:2px}
</style>
</head>
<body>

<section class="sheet sheet--outside">
  <div class="photo photo--panel-edge" role="img" aria-label="Nahaufnahme eines gefrästen MDF-Profils mit heller Kante vor dunklem Hintergrund"></div>
  <svg class="frame-line" width="1143" height="419" aria-hidden="true">
    <polyline points="80,56 168,56 168,290" fill="none" stroke="var(--frame)" stroke-width="2.5"/>
    <polyline points="78,103 78,337 166,337" fill="none" stroke="var(--frame)" stroke-width="2.5"/>
  </svg>

  <h1 class="headline headline--cover">Lüftung als Designelement</h1>
  <div class="photo photo--portrait" role="img" aria-label="Schwarzweiß-Porträt des Tischlers in seiner Küchenausstellung"></div>

  <div class="brand brand--cover">
    <span class="brand__mark"></span>
    <span class="brand__name">RAHMO 2.0 Design<br>Max Feldbauer</span>
  </div>

  <address class="contact">
    Feldbauer Küchen GmbH<br>
    Mühlenweg 7<br>
    77955 Ettenheim<br>
    Tel: 07821 / 555210<br>
    Fax: 07821 / 555211<br>
    info@feldbauer-kuechen.de
  </address>
</section>

<section class="sheet sheet--inside">
  <div class="copy copy--intro">
    <h2>Lüftung als Designelement</h2>
    <p>Man sieht sie oft, gerade im Premiumbereich: Flächenbündig in die Wand eingelassene Küchenschränke und Geräte. Beim Endverbraucher zu Hause schauen die Lösungen leider oftmals nicht mehr so schick aus wie auf Fotos oder in Ausstellungen. Weil es in der Praxis Lüftungsgitter über oder unter den Geräten braucht. Max Feldbauer war das schon länger ein Dorn im Auge. Aktiv wurde er, als ein guter Freund eine Küche kaufen wollte, „wie man sie in Prospekten sieht“ – eben in die Wand eingelassen, aber ohne Lüftungsgitter.</p>
  </div>
  <div class="copy copy--profile">
    <h2>Rahmo 2.0</h2>
    <p>Feldbauer begann zu tüfteln. Als gelernter Tischler kannte er sich mit Holzwerkstoffen aus; durch eine frühere Tätigkeit als Trockenbauer war ihm Gipskarton als Material vertraut. Er experimentierte so lange, bis die aus seiner Sicht optimale Lösung gefunden war.</p>
  </div>

  <div class="photo photo--profile-detail" role="img" aria-label="Schnittansicht der Konstruktion: schwarzes Profil mit Holzkern, eingesetzter Gipskartonplatte und Fräsungen"></div>
  <div class="photo photo--kitchen" role="img" aria-label="Fertige weiße Einbauküche mit flächenbündig in die Wand eingelassenen Schränken, Backöfen und Kochinsel"></div>

  <div class="brand brand--inside">
    <span class="brand__mark"></span>
    <span class="brand__name">RAHMO 2.0 Design<br>Max Feldbauer</span>
  </div>

  <svg class="frame-line" width="1143" height="420" aria-hidden="true">
    <polyline points="826,40 1087,40 1087,199" fill="none" stroke="var(--frame)" stroke-width="3"/>
    <polyline points="610,105 610,338 934,338" fill="none" stroke="var(--frame)" stroke-width="3"/>
  </svg>
  <div class="photo photo--vent-detail" role="img" aria-label="Detail der umlaufenden Lüftungsfuge am Schrankabschluss"></div>
</section>

</body>
</html>
```